Letterhead Design Project

Please see attached logo as well as information below which could be relevant to design. Let me know if you have any questions.

Derek J. Holloman
Estate Planning and Insurance Specialist
Dholloman@brenwickfinancial.com
P: 516-471-2958 F: 516-471-3085
www.brenwickfinancial.com
4300 Maple Ridge Road, Suite 305E
Syosset, New York 11804

```html
<!DOCTYPE html>
<html lang="en">
<head>
<meta charset="utf-8">
<title>Brenwick Financial Group — Stationery</title>
<link href="https://fonts.googleapis.com/css2?family=Cinzel:wght@500&family=Roboto+Condensed:wght@400;700&display=swap" rel="stylesheet">
<style>
  :root{
    --navy:#1f2130;
    --gold:#c9b98b;
    --gold-deep:#b8a574;
    --silver:#b9b9bb;
    --faint:#e6dfcd;
    --paper:#ffffff;
    --backdrop:#d8ccb6;
    --ink:#2a2a2a;
    --muted:#8d8d8d;
  }
  *{box-sizing:border-box;margin:0;padding:0}
  html,body{width:1200px;height:482px;overflow:hidden}
  body{background:var(--backdrop);font-family:"Roboto Condensed",Arial,sans-serif;color:var(--ink);position:relative}
  .sheet{position:absolute;background:var(--paper);overflow:hidden}
  .letterhead{top:8px;width:358px;height:462px}
  .letterhead--light{left:14px}
  .letterhead--dark{left:395px}
  .header-band{position:absolute;left:0;top:0;width:100%;height:86px;background:var(--navy)}

  .brand{position:absolute;display:flex;flex-direction:column;align-items:center;font-family:"Cinzel",serif;font-weight:500;color:var(--gold);line-height:1.05;text-align:center}
  .brand__square{width:30px;height:30px;border:2px solid var(--gold);margin-bottom:4px}
  .brand__name{font-size:9px;letter-spacing:.06em}
  .brand--row{flex-direction:row;align-items:center;gap:5px}
  .brand--row .brand__square{margin:0}
  .brand--ink{color:var(--navy)}
  .brand--ink .brand__square{border-color:var(--navy)}

  .contact{position:absolute;font-size:7px;line-height:11px}
  .contact b{font-weight:700}
  .contact--right{text-align:right;right:22px;top:30px}
  .contact--light{color:#fff;left:264px;top:30px}
  .divider{position:absolute;left:258px;top:31px;width:1px;height:32px;background:var(--silver)}

  .watermark{position:absolute;left:112px;top:175px;width:121px;height:130px;border:9px solid var(--faint);display:flex;align-items:center;justify-content:center;font-family:"Cinzel",serif;font-weight:500;font-size:13px;color:var(--faint);text-align:center;line-height:1.2}

  .footer-wave{position:absolute;left:0;bottom:0;width:100%;height:50px}
  .address{position:absolute;right:14px;bottom:13px;font-size:7px;line-height:9px;text-align:right}
  .address--light{color:#fff}

  .card-label{position:absolute;font-size:6.5px;color:#3a3228;width:147px;text-align:center}
  .card{position:absolute;width:147px;height:84px;border-radius:6px;overflow:hidden;background:var(--navy)}
  .card--gold{background:var(--gold)}
  .card__web{position:absolute;left:0;bottom:12px;width:100%;text-align:center;font-size:5.5px;letter-spacing:.08em;color:#d7d7d7}
  .card--gold .card__web{color:var(--navy)}
  .card__person{position:absolute;right:7px;top:9px;text-align:right;color:#fff;font-size:4.3px;line-height:5.6px}
  .card__name{font-family:"Cinzel",serif;font-size:6.5px;line-height:8px}
  .card__address{position:absolute;right:8px;bottom:4px;text-align:right;font-size:4.3px;line-height:5.2px;color:var(--navy)}

  .envelope{position:absolute;left:790px;top:251px;width:402px;height:221px}
  .envelope__band{position:absolute;left:0;top:46px;width:100%;height:78px;background:var(--navy)}
  .envelope__address{position:absolute;left:22px;top:131px;font-size:7px;line-height:9.5px}
  .envelope__web{position:absolute;left:22px;bottom:9px;font-size:7px;letter-spacing:.08em;color:var(--ink)}
</style>
</head>
<body>

<!-- Letterhead: white with navy footer -->
<section class="sheet letterhead letterhead--light">
  <div class="brand" style="left:16px;top:14px">
    <span class="brand__square"></span>
    <span class="brand__name">BRENWICK<br>FINANCIAL GROUP</span>
  </div>
  <div class="divider"></div>
  <div class="contact contact--right">
    <b>p</b> : 516-471-2958<br>
    <b>f</b> : 516-471-3085<br>
    <b>w</b> : www.brenwickfinancial.com
  </div>
  <div class="watermark">BRENWICK</div>
  <svg class="footer-wave" viewBox="0 0 358 50" preserveAspectRatio="none" aria-hidden="true">
    <path d="M0 12 C120 30 250 18 358 2 L358 6 C250 22 120 34 0 18 Z" fill="var(--silver)"/>
    <path d="M0 20 C120 36 250 22 358 6 L358 50 L0 50 Z" fill="var(--navy)"/>
  </svg>
  <div class="address address--light">4300 Maple Ridge Road<br>Suite 305E, Syosset N Y 11804</div>
</section>

<!-- Letterhead: navy header with gold footer -->
<section class="sheet letterhead letterhead--dark">
  <div class="header-band"></div>
  <div class="brand" style="left:140px;top:12px;width:72px">
    <span class="brand__square"></span>
    <span class="brand__name">BRENWICK<br>FINANCIAL GROUP</span>
  </div>
  <div class="divider"></div>
  <div class="contact contact--light">
    <b>p</b> : 516-471-2958<br>
    <b>f</b> : 516-471-3085<br>
    <b>w</b> : www.brenwickfinancial.com
  </div>
  <div class="watermark">BRENWICK</div>
  <svg class="footer-wave" viewBox="0 0 358 50" preserveAspectRatio="none" aria-hidden="true">
    <path d="M0 8 C120 28 250 14 358 0 L358 4 C250 18 120 32 0 14 Z" fill="var(--navy)"/>
    <path d="M0 16 C120 32 250 20 358 5 L358 9 C250 24 120 36 0 20 Z" fill="var(--silver)"/>
    <path d="M0 22 C120 38 250 24 358 8 L358 50 L0 50 Z" fill="var(--gold)"/>
  </svg>
  <div class="address">4300 Maple Ridge Road<br>Suite 305E, Syosset N Y 11804</div>
</section>

<!-- Business cards -->
<div class="card-label" style="left:845px;top:4px">Front</div>
<div class="card" style="left:845px;top:14px">
  <div class="brand" style="left:12px;top:10px">
    <span class="brand__square" style="width:22px;height:22px;margin-bottom:3px"></span>
    <span class="brand__name" style="font-size:6px">BRENWICK<br>FINANCIAL GROUP</span>
  </div>
  <div class="card__person">
    <div class="card__name">Derek J. Holloman</div>
    Estate Planning and Insurance Specialist<br>
    p : 516-471-2958<br>
    f : 516-471-3085<br>
    e : Dholloman@brenwickfinancial.com<br>
    w : www.brenwickfinancial.com
  </div>
  <svg style="position:absolute;left:0;bottom:0;width:147px;height:32px" viewBox="0 0 147 32" preserveAspectRatio="none" aria-hidden="true">
    <path d="M0 10 C50 20 100 4 147 0 L147 32 L0 32 Z" fill="#fff"/>
    <path d="M0 15 C50 24 100 10 147 6 L147 32 L0 32 Z" fill="var(--silver)"/>
    <path d="M0 19 C50 27 100 14 147 10 L147 32 L0 32 Z" fill="var(--gold)"/>
  </svg>
  <div class="card__address">4300 Maple Ridge Road<br>Suite 305E, Syosset, New York 11804</div>
</div>

<div class="card-label" style="left:1007px;top:4px">Back - 1</div>
<div class="card" style="left:1007px;top:14px">
  <div class="brand brand--row" style="left:14px;top:30px">
    <span class="brand__square" style="width:18px;height:18px"></span>
    <span class="brand__name">BRENWICK FINANCIAL GROUP</span>
  </div>
  <div class="card__web">www.brenwickfinancial.com</div>
</div>

<div class="card-label" style="left:845px;top:107px">Back - 2</div>
<div class="card" style="left:845px;top:117px">
  <div class="brand" style="left:0;top:12px;width:147px">
    <span class="brand__square" style="width:28px;height:28px"></span>
    <span class="brand__name" style="font-size:7px">BRENWICK<br>FINANCIAL GROUP</span>
  </div>
  <div class="card__web" style="bottom:5px">www.brenwickfinancial.com</div>
</div>

<div class="card-label" style="left:1007px;top:107px">Back - 3</div>
<div class="card card--gold" style="left:1007px;top:117px">
  <div class="brand brand--row brand--ink" style="left:14px;top:30px">
    <span class="brand__square" style="width:18px;height:18px"></span>
    <span class="brand__name">BRENWICK FINANCIAL GROUP</span>
  </div>
  <div class="card__web">www.brenwickfinancial.com</div>
</div>

<!-- Envelope -->
<section class="envelope">
  <svg style="position:absolute;left:0;top:0;width:402px;height:221px" viewBox="0 0 402 221" preserveAspectRatio="none" aria-hidden="true">
    <path d="M0 46 C10 10 30 0 60 0 L342 0 C372 0 392 10 402 46 L402 221 L0 221 Z" fill="var(--paper)"/>
    <path d="M0 180 C140 205 280 190 402 168 L402 172 C280 195 140 210 0 186 Z" fill="var(--navy)"/>
    <path d="M0 188 C140 210 280 198 402 176 L402 180 C280 202 140 214 0 192 Z" fill="var(--silver)"/>
    <path d="M0 194 C140 214 280 204 402 184 L402 221 L0 221 Z" fill="var(--gold)"/>
  </svg>
  <div class="brand" style="left:176px;top:12px;width:50px">
    <span class="brand__square" style="width:22px;height:22px;margin:0"></span>
  </div>
  <div class="envelope__band"></div>
  <div class="brand" style="left:24px;top:54px">
    <span class="brand__square" style="width:38px;height:38px"></span>
    <span class="brand__name">BRENWICK<br>FINANCIAL GROUP</span>
  </div>
  <div class="envelope__address">4300 Maple Ridge Road<br>Suite 305E, Syosset, New York 11804</div>
  <div class="envelope__web">www.brenwickfinancial.com</div>
</section>

</body>
</html>
```